TelvoRailCraft: A Swiss railway modelling online shop

I am the developer of TelvoRailCraft, a railway modelling online shop (https://www.telvorailcraft.example) originally developed back in 2004. Today the website needs a complete back-end refresh, which is mostly completed on my side. However I am lacking skills in design, hence my request for support.
The owner of TelvoRailCraft wants to modernize the overall design. He wishes to have it sober, modern and responsive. So you have pretty much "carte blanche" in terms of proposal, the only constraint is to keep the logo as is.
Some products can have variants (e.g. a locomotive can be sold in direct or alternating current), as you can see in the screenshot or when navigating his website.
The current navigation with Brand > Scale > Category > Company can remain, however we would want eventually a page with facet navigation that make it easier to search for a specific article.

```html
<!DOCTYPE html>
<html lang="en">
<head>
<meta charset="utf-8">
<title>TelvoRailCraft – Railway Modelling Shop</title>
<link href="https://fonts.googleapis.com/css2?family=Montserrat:wght@800&family=Poppins:wght@400;500;600&display=swap" rel="stylesheet">
<style>
:root{
  --blue:#2f6598;
  --blue-soft:#e6eef8;
  --ink:#141414;
  --text:#2a2a2a;
  --field:#f0f1f3;
  --footer:#121a23;
  --white:#ffffff;
}
*{box-sizing:border-box;margin:0;padding:0}
html,body{width:1058px;height:1200px;overflow:hidden;background:var(--white)}
body{position:relative;font-family:"Poppins",sans-serif;color:var(--text)}
a{color:inherit;text-decoration:none}

.site-header{position:absolute;left:0;top:0;width:1058px;height:115px;background:var(--white)}
.brand{position:absolute;left:120px;top:40px;display:flex;align-items:center;gap:9px;font-size:18px;font-weight:600;color:var(--blue)}
.brand-mark{width:16px;height:16px;background:var(--blue)}
.search{position:absolute;left:527px;top:19px;width:224px;height:38px;border-radius:19px;background:var(--field);display:flex;align-items:center;padding-left:19px;gap:7px;font-size:11px;color:#707070}
.filter-btn{position:absolute;left:755px;top:20px;width:34px;height:34px;border-radius:50%;background:var(--blue);display:flex;align-items:center;justify-content:center}
.login-btn{position:absolute;left:843px;top:19px;width:87px;height:38px;border-radius:19px;background:var(--blue);color:var(--white);display:flex;align-items:center;justify-content:center;gap:4px;font-size:13px;font-weight:500}
.main-nav{position:absolute;left:361px;top:76px;display:flex;gap:0;font-size:13px;font-weight:500;color:var(--ink)}
.main-nav a{position:absolute;white-space:nowrap}
.currency{color:var(--blue);font-weight:600}

.hero{position:absolute;left:0;top:115px;width:1058px;height:454px;overflow:hidden}
.hero-photo{position:absolute;inset:0;background:
  radial-gradient(ellipse 320px 260px at 820px 260px,#3a3d40 0%,rgba(40,40,42,.85) 45%,rgba(0,0,0,0) 75%),
  radial-gradient(ellipse 260px 200px at 1000px 300px,#c4552a 0%,rgba(196,85,42,0) 70%),
  radial-gradient(ellipse 380px 200px at 200px 420px,#8a2a22 0%,rgba(138,42,34,0) 70%),
  linear-gradient(160deg,#5c6b3a 0%,#3b3a2c 35%,#2c2624 60%,#4a2e22 100%)}
.hero-shade{position:absolute;inset:0;background:linear-gradient(90deg,rgba(0,0,0,.45) 0%,rgba(0,0,0,.25) 55%,rgba(0,0,0,0) 80%)}
.hero-title{position:absolute;left:125px;top:108px;font-family:"Montserrat",sans-serif;font-weight:800;font-size:37px;line-height:48px;color:var(--white)}
.hero-sub{position:absolute;left:128px;top:225px;font-size:17px;font-weight:600;line-height:28px;color:var(--white)}
.hero-cta{position:absolute;left:130px;top:306px;width:134px;height:38px;border-radius:19px;background:var(--blue);color:var(--white);font-size:12px;font-weight:600;display:flex;align-items:center;justify-content:center;letter-spacing:.2px}

.intro-title{position:absolute;left:0;top:648px;width:1058px;text-align:center;font-family:"Montserrat",sans-serif;font-weight:800;font-size:29px;color:var(--ink)}
.intro-title span{color:var(--blue)}
.intro-text{position:absolute;left:199px;top:711px;width:660px;text-align:center;font-size:12px;line-height:23px;color:var(--ink)}

.feature{position:absolute;top:777px;width:260px;text-align:center}
.feature-icon{width:82px;height:82px;border-radius:50%;background:var(--blue-soft);margin:0 auto;display:flex;align-items:center;justify-content:center}
.feature-icon.is-primary{background:var(--blue)}
.feature h3{margin-top:23px;font-size:17px;font-weight:500;color:var(--ink)}
.feature p{margin-top:12px;font-size:12px;line-height:22.5px;color:var(--ink)}
.feature p a{color:var(--blue)}

.site-footer{position:absolute;left:0;top:1053px;width:1058px;height:147px;background:var(--footer);color:var(--white);font-weight:500;font-size:13px}
.footer-nav a{position:absolute;top:41px;white-space:nowrap}
.footer-line{position:absolute;left:0;width:1058px;text-align:center}
.footer-line u{text-underline-offset:3px}
</style>
</head>
<body>

<header class="site-header">
  <a class="brand" href="https://www.telvorailcraft.example"><span class="brand-mark"></span>TelvoRailCraft</a>
  <div class="search">
    <svg width="11" height="11" viewBox="0 0 12 12"><circle cx="5" cy="5" r="3.8" fill="none" stroke="#555" stroke-width="1.6"/><line x1="8" y1="8" x2="11" y2="11" stroke="#555" stroke-width="1.6"/></svg>
    Search for
  </div>
  <div class="filter-btn">
    <svg width="18" height="16" viewBox="0 0 18 16" fill="none" stroke="#fff" stroke-width="1.2"><line x1="1" y1="3" x2="17" y2="3"/><line x1="1" y1="8" x2="17" y2="8"/><line x1="1" y1="13" x2="17" y2="13"/><circle cx="11" cy="3" r="1.8" fill="#2f6598"/><circle cx="6" cy="8" r="1.8" fill="#2f6598"/><circle cx="11" cy="13" r="1.8" fill="#2f6598"/></svg>
  </div>
  <a class="login-btn" href="#">
    <svg width="10" height="11" viewBox="0 0 10 11" fill="#fff"><circle cx="5" cy="3" r="2.6"/><path d="M0 11c0-3 2-4.8 5-4.8s5 1.8 5 4.8z"/></svg>Login
  </a>
  <nav class="main-nav">
    <a style="left:0">Welcome</a>
    <a style="left:80px">Catalog</a>
    <a style="left:152px">Occasions</a>
    <a style="left:239px">Spare parts</a>
    <a style="left:336px">Shop</a>
    <a style="left:392px">Service</a>
    <a style="left:458px">Contact Us</a>
    <a class="currency" style="left:556px">€</a>
  </nav>
</header>

<section class="hero">
  <div class="hero-photo" role="img" aria-label="Close-up photograph of a model steam locomotive with a red front on track among blurred red foliage"></div>
  <div class="hero-shade"></div>
  <h1 class="hero-title">OUR ONLY CONCERN IS<br>YOUR SATISFACTION</h1>
  <p class="hero-sub">KORVATH SRX LOCOMOTIVE TYPE FC 2X3/4 (CE 6/8 I)<br>DIGITAL ALTERNATING CURRENT WITH SOUND EFFECTS</p>
  <a class="hero-cta" href="#">CONTACT US</a>
</section>

<h2 class="intro-title">THE WORLD OF MODEL TRAINS <span>AT YOUR FINGERTIPS</span></h2>
<p class="intro-text">This site presents a selection of new equipment from the catalogs of the brands offered. Other models and references, even if not listed here, can be ordered upon request.</p>

<article class="feature" style="left:103px">
  <div class="feature-icon">
    <svg width="44" height="44" viewBox="0 0 44 44" fill="none" stroke="#2f6598" stroke-width="1.3" stroke-linejoin="round"><path d="M22 2l1.8 3.6 4 .6-2.9 2.8.7 4-3.6-1.9-3.6 1.9.7-4-2.9-2.8 4-.6z"/><path d="M9 7l1.3 2.6 2.9.4-2.1 2 .5 2.9L9 13.5l-2.6 1.4.5-2.9-2.1-2 2.9-.4z"/><path d="M35 7l1.3 2.6 2.9.4-2.1 2 .5 2.9L35 13.5l-2.6 1.4.5-2.9-2.1-2 2.9-.4z"/><circle cx="22" cy="29" r="13"/><circle cx="22" cy="25" r="4.5"/><path d="M13.5 38.5c1.5-4.5 4.5-7 8.5-7s7 2.5 8.5 7"/></svg>
  </div>
  <h3>Customer Service</h3>
  <p>Feel free to <a href="#">contact me</a> or use the form provided for this purpose for any order or specific question.</p>
</article>

<article class="feature" style="left:399px">
  <div class="feature-icon is-primary">
    <svg width="58" height="40" viewBox="0 0 58 40" fill="none" stroke="#fff" stroke-width="1.6" stroke-linejoin="round" stroke-linecap="round"><path d="M33 2v12M29 10l4 4 4-4"/><rect x="2" y="20" width="6" height="16"/><path d="M8 22h10c3 0 6 3 9 3h6c2 0 2 3 0 3h-9M8 34h16l24-10c3-1.5 1-5-2-4l-13 5"/></svg>
  </div>
  <h3>Pre-owned Models</h3>
  <p>Discover our selection of pre-owned models via the <a href="#">'Pre-owned'</a> link. You might find that rare piece that will complete your collection.</p>
</article>

<article class="feature" style="left:709px">
  <div class="feature-icon">
    <svg width="46" height="46" viewBox="0 0 46 46" fill="none" stroke="#2f6598" stroke-width="1.4" stroke-linejoin="round"><path d="M26 38H6V8h6M26 8h6v12"/><rect x="12" y="4" width="14" height="7" rx="2"/><line x1="11" y1="19" x2="27" y2="19"/><line x1="11" y1="25" x2="22" y2="25"/><line x1="11" y1="31" x2="20" y2="31"/><circle cx="33" cy="33" r="10"/><line x1="33" y1="31" x2="33" y2="38"/><circle cx="33" cy="27.5" r=".8" fill="#2f6598"/></svg>
  </div>
  <h3>Further Information</h3>
  <p>For any further information, <a href="#">I am at your disposal!</a></p>
</article>

<footer class="site-footer">
  <nav class="footer-nav">
    <a style="left:265px">Welcome</a>
    <a style="left:345px">Catalog</a>
    <a style="left:417px">Occasions</a>
    <a style="left:504px">Spare parts</a>
    <a style="left:601px">Shop</a>
    <a style="left:657px">Service</a>
    <a style="left:723px">Contact Us</a>
  </nav>
  <p class="footer-line" style="top:75px">Welcome, you are the <u>609490th</u> visitor!</p>
  <p class="footer-line" style="top:109px">Copyright@2025.All Rights Reserved</p>
</footer>

</body>
</html>
```